Marlo Tidy Yard Website

We need a website design for this new company. I've attached the company logo. This company is in the construction industry that provides general labor, maintenance and cleaning for construction sites. We want a clean and simple website that can be easy to navigate.

Target Market(s)

Construction industry

Industry/Entity Type

Construction

Number of Pages Required

2 page

Font styles to use
Sans Serif

```html
<!DOCTYPE html>
<html lang="en">
<head>
<meta charset="utf-8">
<title>Marlo Tidy Yard</title>
<link href="https://fonts.googleapis.com/css2?family=Poppins:wght@400;500;600;700&display=swap" rel="stylesheet">
<style>
:root{
  --navy:#0c0a6e;
  --orange:#ff6a00;
  --text:#2a2a3a;
  --muted:#555566;
  --light:#f5f5f5;
  --cream:#fff8e6;
  --line:#d6d6de;
  --white:#ffffff;
}
*{margin:0;padding:0;box-sizing:border-box}
html,body{width:1200px;height:2579px;overflow:hidden}
body{font-family:'Poppins',Arial,sans-serif;color:var(--text);background:var(--white);position:relative}
.abs{position:absolute}

/* header */
.site-header{position:absolute;left:0;top:0;width:1200px;height:93px;background:var(--white)}
.brand{position:absolute;left:143px;top:26px;display:flex;align-items:center;gap:10px}
.brand-mark{width:22px;height:22px;background:var(--orange)}
.brand-name{font-size:26px;font-weight:700;color:var(--navy);line-height:1}
.main-nav a{position:absolute;top:52px;font-size:17px;color:var(--navy);text-decoration:none}
.main-nav .active{font-weight:500}
.header-contact{position:absolute;top:36px;display:flex;gap:12px;align-items:flex-start}
.header-contact .label{font-size:13px;color:var(--orange);line-height:1.2}
.header-contact .value{font-size:16px;color:var(--text);line-height:1.3}

/* hero */
.hero{position:absolute;left:0;top:93px;width:1200px;height:510px;overflow:hidden}
.hero-photo{position:absolute;inset:0;background:linear-gradient(100deg,#2f5db8 0%,#51627c 25%,#6b655a 50%,#8a7a62 75%,#9a948a 100%)}
.hero-wave{position:absolute;left:0;bottom:0}
.hero-caption{position:absolute;left:0;width:1200px;top:404px;text-align:center;font-size:25px;font-weight:500;color:var(--white);letter-spacing:.5px;z-index:2}
.hero-dots{position:absolute;top:451px;left:576px;display:flex;gap:22px;z-index:2}
.hero-dots span{width:12px;height:12px;background:var(--white);border-radius:2px}

/* headings */
.section-title{font-size:34px;font-weight:600;color:var(--navy);line-height:1.2}
.section-title em{font-style:normal;color:var(--orange)}
.title-rule{height:3px;background:var(--line);border-radius:2px}

.btn{position:absolute;display:flex;align-items:center;justify-content:center;background:var(--navy);color:var(--white);font-size:15px;font-weight:500;border-radius:18px;height:36px}

/* about */
.about-title{left:143px;top:657px}
.about-lead{left:143px;top:742px;font-size:12px;font-weight:600;line-height:21px;color:#111;white-space:nowrap}
.about-body{left:143px;top:786px;font-size:12px;line-height:21.3px;color:var(--muted);white-space:nowrap}
.about-photo{left:743px;top:671px;width:316px;height:316px;border-radius:50%;background:radial-gradient(circle at 40% 40%,#f2efe6,#c9b99a 55%,#6f7a5c)}

/* services */
.services{position:absolute;left:0;top:1049px;width:1200px;height:679px;background:var(--light)}
.service-card{position:absolute;top:149px;width:290px;height:367px;background:var(--white);border-radius:6px;box-shadow:0 2px 8px rgba(0,0,0,.08)}
.service-photo{height:172px;border-radius:6px 6px 0 0}
.service-icon{position:absolute;left:107px;top:134px;width:76px;height:76px;border-radius:50%;display:flex;align-items:center;justify-content:center}
.service-name{position:absolute;top:222px;width:100%;text-align:center;font-size:15px;font-weight:600}
.service-text{position:absolute;top:252px;left:0;right:0;text-align:center;font-size:12px;line-height:20.5px;color:var(--muted);white-space:nowrap}
.service-more{position:absolute;left:130px;bottom:-15px;width:30px;height:30px;border-radius:50%;display:flex;align-items:center;justify-content:center}

/* contact */
.quick-contact{position:absolute;left:0;top:1728px;width:1200px;height:512px;background:linear-gradient(180deg,#fffbee 0%,#fff3d4 60%,#ffe7a8 100%)}
.contact-intro{position:absolute;left:260px;top:138px;width:680px;text-align:center;font-size:13px;line-height:1.75;color:var(--text)}
.field{position:absolute;height:41px;background:var(--white);border:1px solid var(--line);border-radius:4px;display:flex;align-items:center;font-size:11px;color:#444}
.field .ico{width:36px;height:100%;display:flex;align-items:center;justify-content:center;border-right:1px solid var(--line);margin-right:10px}
.field.message{align-items:flex-start}
.field.message .ico{height:30px;border-right:none}
.field.message span.ph{padding-top:9px}
.btn-submit{background:var(--orange);font-size:13px;letter-spacing:.5px;height:34px;border-radius:17px}

/* footer */
.site-footer{position:absolute;left:0;top:2240px;width:1200px;height:290px;background:var(--navy);color:var(--white)}
.footer-heading{position:absolute;top:58px;font-size:15px;font-weight:500}
.footer-heading::after{content:"";display:block;width:120px;height:2px;background:#5a58a8;margin-top:6px}
.footer-list{position:absolute;left:143px;top:105px;list-style:none;font-size:13px}
.footer-list li{display:flex;gap:20px;align-items:flex-start;line-height:1.55}
.footer-list svg{flex:none;margin-top:2px}
.map{position:absolute;left:464px;top:105px;width:329px;height:141px;border:3px solid #3f3d95;background:linear-gradient(135deg,#e8e6df,#d9e4d0 60%,#e9dfc6)}
.social{position:absolute;left:906px;top:104px;display:flex;gap:5px}
.social span{width:24px;height:24px;border-radius:50%;background:#3f3d95}
.footer-brand{position:absolute;left:906px;top:150px;display:flex;align-items:center;gap:8px}
.footer-brand .brand-mark{width:18px;height:18px}
.footer-brand .brand-name{font-size:20px;color:var(--white)}
.copyright{position:absolute;left:0;top:2530px;width:1200px;height:49px;background:var(--orange);color:var(--white);font-size:12px;display:flex;align-items:center;justify-content:center}
</style>
</head>
<body>

<header class="site-header">
  <div class="brand"><span class="brand-mark"></span><span class="brand-name">Marlo Tidy Yard</span></div>
  <nav class="main-nav">
    <a class="active" href="#" style="left:487px">Home</a>
    <a href="#" style="left:576px">Services</a>
  </nav>
  <div class="header-contact" style="left:671px">
    <svg width="30" height="30" viewBox="0 0 24 24" fill="none" stroke="#0c0a6e" stroke-width="1.6"><path d="M5 3h3l2 5-2 1.5a11 11 0 0 0 6.5 6.5L16 14l5 2v3a2 2 0 0 1-2 2A17 17 0 0 1 3 5a2 2 0 0 1 2-2z"/><path d="M14 3a7 7 0 0 1 7 7M14 7a3 3 0 0 1 3 3"/></svg>
    <div><div class="label">Request call back</div><div class="value">(123) 456-78120</div></div>
  </div>
  <div class="header-contact" style="left:855px">
    <svg width="28" height="28" viewBox="0 0 24 24" fill="none" stroke="#0c0a6e" stroke-width="1.6"><path d="M3 9l9-6 9 6v11H3z"/><path d="M3 9l9 6 9-6"/><rect x="7" y="6" width="10" height="6"/></svg>
    <div><div class="label">Write us</div><div class="value">info@marlotidyyard.com</div></div>
  </div>
</header>

<section class="hero">
  <div class="hero-photo" role="img" aria-label="Two site workers in orange high-visibility gear working beside an excavator"></div>
  <svg class="hero-wave" width="1200" height="110" viewBox="0 0 1200 110" preserveAspectRatio="none">
    <path d="M0 110 L0 106 C200 62 400 62 600 74 C800 86 1000 82 1200 42 L1200 110 Z" fill="#ffffff"/>
  </svg>
  <div class="hero-caption">Helping You And Your House Become Better Acquainted.</div>
  <div class="hero-dots"><span></span><span></span></div>
</section>

<h2 class="section-title abs about-title">About Marlo <em>Tidy Yard</em></h2>
<div class="title-rule abs" style="left:143px;top:710px;width:250px"></div>
<p class="abs about-lead">Lorem ipsum dolor sit amet, consectetuer adipiscing elit, sed diam nonmmy nih euismod<br>tincunt ut laoreet dolore magna aliquam erat volutpat Ut wisi enim ad minim veniam.</p>
<p class="abs about-body">Lorem ipsum dolor sit amet, consectetuer adipiscing elit, sed diam nonummy nibh euismod<br>tincidunt ut laoreet dolore magna aliquam erat volutpat. Ut wisi enim ad minim veniam, quis<br>nostrud exerci tation ullamcorper suscipit lobortis nisl ut aliquip ex ea commodo consequat.<br>Duis autem vel eum iriure dolot laoreet dolore magna aliquam erat volutpat. Ut wisi enim ad<br>minim veniam, quis nostrud exerci tation ullamcorper suscipit lobortis nisl ut aliquip ex ea<br>commodo consequat. Duis autem vel eum iriure dolor in hendrerit in vulputate velit esse<br>molestie consequat, vel illum dolore eu feugiat nulla facilr.</p>
<a class="btn" style="left:142px;top:950px;width:152px">Contact Us Today</a>
<div class="abs about-photo" role="img" aria-label="Builders in hard hats reviewing site plans on a table"></div>

<section class="services">
  <h2 class="section-title abs" style="left:0;width:1200px;text-align:center;top:45px">Our <em>Services</em></h2>
  <div class="title-rule abs" style="left:535px;top:88px;width:130px"></div>

  <article class="service-card" style="left:143px">
    <div class="service-photo" role="img" aria-label="Workers on a building site with safety railings" style="background:linear-gradient(160deg,#dfe3e8,#a9a088 60%,#8b6a4a)"></div>
    <div class="service-icon" style="background:var(--navy)"><svg width="40" height="40" viewBox="0 0 24 24" fill="#ff6a00"><circle cx="8" cy="8" r="3"/><circle cx="16" cy="8" r="3"/><path d="M3 20a5 5 0 0 1 10 0zM11 20a5 5 0 0 1 10 0z"/></svg></div>
    <h3 class="service-name" style="color:var(--navy)">General Labor</h3>
    <p class="service-text">Lorem ipsum dolor sit consectetudipiscing<br>sed diam nonmmy nibh euismod tincunt<br>ut looareet dolore meagna consectetuer<br>adipiscing &nbsp;sed diam nonmmy.</p>
    <div class="service-more" style="background:var(--navy)"><svg width="12" height="12" viewBox="0 0 12 12" stroke="#fff" stroke-width="2"><path d="M6 1v10M1 6h10"/></svg></div>
  </article>

  <article class="service-card" style="left:456px">
    <div class="service-photo" role="img" aria-label="Workers shovelling sand under a blue sky" style="background:linear-gradient(180deg,#3f7fd6,#8fb6e8 55%,#e9e6e0)"></div>
    <div class="service-icon" style="background:var(--orange)"><svg width="40" height="40" viewBox="0 0 24 24" fill="#0c0a6e"><circle cx="10" cy="4" r="2.5"/><path d="M8 8h4l2 6-2 1-1.5-3-1.5 3 1 6H8l-1-6 1-5z"/><path d="M14 12l5 7" stroke="#0c0a6e" stroke-width="1.5"/><path d="M17 19h5v2h-5z"/></svg></div>
    <h3 class="service-name" style="color:var(--orange)">Maintenance &nbsp;Works</h3>
    <p class="service-text">Lorem ipsum dolor sit consectetudipiscing<br>sed diam nonmmy nibh euismod tincunt<br>ut looareet dolore meagna consectetuer<br>adipiscing &nbsp;sed diam nonmmy.</p>
    <div class="service-more" style="background:var(--orange)"><svg width="12" height="12" viewBox="0 0 12 12" stroke="#fff" stroke-width="2"><path d="M6 1v10M1 6h10"/></svg></div>
  </article>

  <article class="service-card" style="left:769px">
    <div class="service-photo" role="img" aria-label="Worker sweeping a concrete floor with a broom" style="background:linear-gradient(150deg,#e6e4df,#c9c6bf 55%,#6f8a5e)"></div>
    <div class="service-icon" style="background:var(--orange)"><svg width="40" height="40" viewBox="0 0 24 24" fill="#0c0a6e"><circle cx="9" cy="4" r="2.5"/><path d="M7 8h4l1 6-2 1v6H7v-7l-1-1z"/><path d="M12 9l7 9" stroke="#0c0a6e" stroke-width="1.5"/><path d="M17 18h5l-1 3h-4z"/></svg></div>
    <h3 class="service-name" style="color:var(--orange)">Cleaning For Construction Sites</h3>
    <p class="service-text">Lorem ipsum dolor sit consectetudipiscing<br>sed diam nonmmy nibh euismod tincunt<br>ut looareet dolore meagna consectetuer<br>adipiscing &nbsp;sed diam nonmmy.</p>
    <div class="service-more" style="background:var(--orange)"><svg width="12" height="12" viewBox="0 0 12 12" stroke="#fff" stroke-width="2"><path d="M6 1v10M1 6h10"/></svg></div>
  </article>

  <a class="btn" style="left:524px;top:562px;width:152px">Contact Us Today</a>
</section>

<section class="quick-contact">
  <h2 class="section-title abs" style="left:0;width:1200px;text-align:center;top:60px">Quick <em>Contact</em></h2>
  <div class="title-rule abs" style="left:540px;top:112px;width:120px;background:#e3dccb"></div>
  <p class="contact-intro">Lorem ipsum dolor sit amet, consectetuer adipiscing elit, sed diam nonmmy nibh euismod tincunt ut laoreet dolore magna aliquam erat volutpat Ut wisi enim ad minim veniam.</p>

  <div class="field" style="left:303px;top:201px;width:288px"><span class="ico"><svg width="12" height="12" viewBox="0 0 24 24" fill="#0c0a6e"><circle cx="12" cy="7" r="5"/><path d="M2 23a10 10 0 0 1 20 0z"/></svg></span><span>First Name*</span></div>
  <div class="field" style="left:607px;top:201px;width:289px"><span class="ico"><svg width="12" height="12" viewBox="0 0 24 24" fill="#0c0a6e"><circle cx="12" cy="7" r="5"/><path d="M2 23a10 10 0 0 1 20 0z"/></svg></span><span>Last Name*</span></div>
  <div class="field" style="left:303px;top:256px;width:288px"><span class="ico"><svg width="12" height="12" viewBox="0 0 24 24" fill="#0c0a6e"><path d="M5 2h4l2 6-3 2a12 12 0 0 0 6 6l2-3 6 2v4a2 2 0 0 1-2 2A19 19 0 0 1 3 4a2 2 0 0 1 2-2z"/></svg></span><span>Your Phone*</span></div>
  <div class="field" style="left:607px;top:256px;width:289px"><span class="ico"><svg width="12" height="12" viewBox="0 0 24 24" fill="#0c0a6e"><path d="M2 5h20v2l-10 6L2 7z"/><path d="M2 9l10 6 10-6v10H2z"/></svg></span><span>Your Email*</span></div>
  <div class="field message" style="left:303px;top:311px;width:593px;height:84px"><span class="ico"><svg width="13" height="12" viewBox="0 0 24 22" fill="#0c0a6e"><path d="M2 2h14v10H7l-4 3v-3H2z"/><path d="M18 6h4v10h-1v3l-4-3h-7v-2h8z"/></svg></span><span class="ph">Your Message*</span></div>

  <a class="btn btn-submit" style="left:531px;top:414px;width:138px">SUBMIT NOW</a>
</section>

<footer class="site-footer">
  <h4 class="footer-heading" style="left:143px">Contact Details</h4>
  <ul class="footer-list">
    <li style="margin-bottom:12px"><svg width="12" height="16" viewBox="0 0 12 16" fill="#fff"><path d="M6 0a6 6 0 0 1 6 6c0 4-6 10-6 10S0 10 0 6a6 6 0 0 1 6-6zm0 3a3 3 0 1 0 0 6 3 3 0 0 0 0-6z"/></svg><span>Street Name City Name<br>State Zipcode</span></li>
    <li style="margin-bottom:14px"><svg width="14" height="14" viewBox="0 0 24 24" fill="#fff"><path d="M5 2h4l2 6-3 2a12 12 0 0 0 6 6l2-3 6 2v4a2 2 0 0 1-2 2A19 19 0 0 1 3 4a2 2 0 0 1 2-2z"/></svg><span>(123) 456-78120</span></li>
    <li style="margin-bottom:14px"><svg width="14" height="14" viewBox="0 0 24 24" fill="#fff"><path d="M6 2h12v6H6z"/><path d="M2 9h20v9h-4v4H6v-4H2zm6 6v5h8v-5z"/></svg><span>(123) 456-78120</span></li>
    <li><svg width="14" height="14" viewBox="0 0 24 24" fill="none" stroke="#fff" stroke-width="2"><path d="M3 9l9-6 9 6v11H3z"/><path d="M3 9l9 6 9-6"/></svg><span>info@marlotidyyard.com</span></li>
  </ul>

  <h4 class="footer-heading" style="left:464px;top:52px">Location Map</h4>
  <div class="map" role="img" aria-label="Street map showing the office location with a pin"></div>

  <h4 class="footer-heading" style="left:906px">Follow Us</h4>
  <div class="social"><span></span><span></span><span></span><span></span></div>
  <div class="footer-brand"><span class="brand-mark"></span><span class="brand-name">Marlo Tidy Yard</span></div>
</footer>

<div class="copyright">Copyright © 2019 Marlo Tidy Yard. All Rights Reserved.</div>

</body>
</html>
```